Creative, New Pizza Box Design

Zo Brightbite Foods is a new Australian start-up which is going to focus on never before seen on the market low-carb food products.

The first product to hit the market will be frozen pizza. So will need to stand out from other products on the market.

Our products are made from simple natural ingredients and aren't overly processed or artificial. The logo should tell a story to end customers who are frustrated by the lack of low-carb options when shopping. It should illustrate to customers that the products are wholesome, healthy and low-carb.
And the design needs to communicate health and simplicity.

We would like to see a design for a pizza box. The logo attached (both text and image) is to be positioned in the top left hand corner rotated counter-clockwise. And the text on its own should be on the top (feel free to add more the text as well). The orange and green from the logo need to be used as the colour scheme and the background should be some form of white, beige or mushroom colour. The only thing that you don't need to worry about is the pizza image itself. You can us a placeholder image until I get a professional photo. I have attached an example which can be used.

Any further questions, don't hesitate to post them.

Target Market(s)

People interested in diet and healthy eating. Often people who also lead busy lives and don't have the time to spend cooking.

Industry/Entity Type

Product

Requirements
Must have
• - The logo attached
• - incorporation of the logo colour scheme
Nice to have
• - use of leafy imagery or fruit/vegetable images in the corners or around the border

```html
<!DOCTYPE html>
<html lang="en">
<head>
<meta charset="utf-8">
<title>Zo Brightbite Foods – Pizza Box</title>
<link href="https://fonts.googleapis.com/css2?family=Ubuntu:wght@500;700&family=Baloo+2:wght@700&display=swap" rel="stylesheet">
<style>
  :root {
    --stage: #d9d9d9;
    --lid-white: #fbfbfb;
    --sketch-grey: #ececec;
    --brand-green: #21a035;
    --brand-green-dark: #17792a;
    --ribbon-green: #5cb52f;
    --ink-black: #0b0b0b;
    --crust-orange: #f39a1c;
    --sauce-red: #e23a22;
    --text-white: #ffffff;
  }
  html, body {
    margin: 0;
    padding: 0;
    width: 1200px;
    height: 1000px;
    overflow: hidden;
    background: var(--stage);
  }
  .box-net {
    position: relative;
    width: 1200px;
    height: 1000px;
  }
  .lid {
    position: absolute;
    left: 180px;
    top: 60px;
    width: 640px;
    height: 640px;
    background: var(--lid-white);
    overflow: hidden;
  }
  .lid-pattern {
    position: absolute;
    inset: 0;
    background: radial-gradient(circle at 70% 40%, var(--lid-white) 0%, var(--sketch-grey) 100%);
  }
  .pizza-art {
    position: absolute;
    left: 0;
    top: 0;
    width: 640px;
    height: 640px;
  }
  .tagline-ribbon {
    position: absolute;
    left: 250px;
    top: 108px;
    width: 330px;
    height: 60px;
    transform: rotate(-9deg);
  }
  .tagline-ribbon svg { position: absolute; inset: 0; }
  .tagline-text {
    position: absolute;
    inset: 0;
    display: flex;
    align-items: center;
    justify-content: center;
    font-family: "Baloo 2", sans-serif;
    font-weight: 700;
    font-size: 28px;
    color: var(--text-white);
    letter-spacing: 0.5px;
  }
  .brand-badge {
    position: absolute;
    left: 225px;
    top: 200px;
    width: 220px;
    height: 220px;
    border-radius: 50%;
    background: var(--ink-black);
    display: flex;
    align-items: center;
    justify-content: center;
    text-align: center;
  }
  .brand-badge-name {
    font-family: "Ubuntu", sans-serif;
    font-weight: 700;
    font-size: 26px;
    line-height: 1.15;
    color: var(--brand-green);
    width: 160px;
  }
  .front-panel {
    position: absolute;
    left: 180px;
    top: 700px;
    width: 640px;
    height: 150px;
    background: linear-gradient(180deg, var(--brand-green) 0%, var(--brand-green-dark) 100%);
    border-radius: 0 0 22px 22px;
    display: flex;
    align-items: center;
    justify-content: center;
  }
  .front-panel::before {
    content: "";
    position: absolute;
    left: 50%;
    top: -26px;
    width: 52px;
    height: 52px;
    margin-left: -26px;
    border-radius: 50%;
    background: var(--lid-white);
  }
  .front-panel-name {
    font-family: "Ubuntu", sans-serif;
    font-weight: 700;
    font-size: 54px;
    color: var(--text-white);
    margin-top: 12px;
  }
  .side-panel {
    position: absolute;
    left: 820px;
    top: 60px;
    width: 130px;
    height: 640px;
    background: linear-gradient(90deg, var(--brand-green-dark) 0%, var(--brand-green) 100%);
    border-radius: 0 18px 18px 0;
    display: flex;
    align-items: center;
    justify-content: center;
  }
  .side-panel-name {
    font-family: "Ubuntu", sans-serif;
    font-weight: 700;
    font-size: 44px;
    color: var(--text-white);
    white-space: nowrap;
    transform: rotate(-90deg);
    opacity: 0.9;
  }
</style>
</head>
<body>
<main class="box-net">
  <section class="lid">
    <div class="lid-pattern" role="img" aria-label="Light grey hand-drawn sketches of pizza slices, cheese, tomatoes and herbs scattered over the lid"></div>

    <svg class="pizza-art" viewBox="0 0 640 640" role="img" aria-label="Illustrated pepperoni and mushroom pizza, upper half showing above the front flap">
      <defs>
        <radialGradient id="pizza-fill" cx="50%" cy="50%" r="50%">
          <stop offset="0%" stop-color="#f6c160"/>
          <stop offset="70%" stop-color="#f2a63a"/>
          <stop offset="86%" stop-color="var(--sauce-red)"/>
          <stop offset="92%" stop-color="var(--crust-orange)"/>
          <stop offset="100%" stop-color="#e57a12"/>
        </radialGradient>
      </defs>
      <circle cx="250" cy="640" r="390" fill="url(#pizza-fill)"/>
    </svg>

    <div class="tagline-ribbon">
      <svg viewBox="0 0 330 60" width="330" height="60" aria-hidden="true">
        <polygon points="0,14 30,14 30,54 0,54 14,34" fill="var(--brand-green-dark)"/>
        <polygon points="330,14 300,14 300,54 330,54 316,34" fill="var(--brand-green-dark)"/>
        <rect x="20" y="4" width="290" height="44" fill="var(--ribbon-green)"/>
      </svg>
      <div class="tagline-text">fresh healthy taste</div>
    </div>

    <div class="brand-badge">
      <span class="brand-badge-name">Zo Brightbite Foods</span>
    </div>
  </section>

  <section class="side-panel">
    <span class="side-panel-name">Zo Brightbite Foods</span>
  </section>

  <section class="front-panel">
    <span class="front-panel-name">Zo Brightbite Foods</span>
  </section>
</main>
</body>
</html>
```